BRIM Exterior Coatings

double sided. the front i want the name of the business each word on a new line with the BRIM being bigger. id like teal, black and white colors. the back i want my contact info. Flat, no gloss. Something professional and I want to feel the letters bump put of the card. if possible maybe a paint sprayer in corner. not a car paint spray. (no tank on top of gun)
no vehicle paint sprayers. that means no tank on top of the gun. doesn't have to have a sprayer. black/dark background on the front. white back ground on back with info

```html
<!DOCTYPE html>
<html lang="en">
<head>
<meta charset="utf-8">
<title>BRIM Exterior Coatings — Business Card</title>
<link rel="stylesheet" href="https://fonts.googleapis.com/css2?family=Poppins:wght@400;500;700;800&display=swap">
<style>
  :root {
    --stage: #161616;
    --card-dark: #0d0d0d;
    --sheen-core: #c4c4c4;
    --sheen-mid: #8e8e8e;
    --sheen-edge: #353535;
    --ink-dark: #1a1a1a;
    --card-light: #ffffff;
    --teal: #1a9a96;
    --black: #141414;
  }
  * { margin: 0; padding: 0; box-sizing: border-box; }
  html, body {
    width: 1200px; height: 1200px; overflow: hidden;
    background: var(--stage);
    font-family: "Poppins", sans-serif;
  }
  .stage {
    width: 1200px; height: 1200px;
    display: flex; flex-direction: column; align-items: center; justify-content: center;
    gap: 44px;
  }
  .card {
    width: 900px; height: 514px;
    border-radius: 26px;
    position: relative;
    overflow: hidden;
  }
  /* Front */
  .card-front {
    background:
      radial-gradient(ellipse 520px 330px at 50% 50%,
        var(--sheen-core) 0%, var(--sheen-mid) 38%, var(--sheen-edge) 70%, var(--card-dark) 100%),
      var(--card-dark);
    display: flex; align-items: center; justify-content: center;
  }
  .wordmark {
    text-transform: uppercase;
    font-weight: 800;
    line-height: 0.95;
    letter-spacing: 0.04em;
    text-align: left;
  }
  .wordmark .wordmark-lead { display: block; font-size: 112px; letter-spacing: 0.02em; }
  .wordmark .wordmark-line { display: block; font-size: 46px; }
  .card-front .wordmark { color: var(--ink-dark); }

  /* Back */
  .card-back { background: var(--card-light); }
  .card-back .wordmark {
    position: absolute; right: 70px; top: 118px;
    color: var(--teal);
  }
  .card-back .wordmark .wordmark-lead { font-size: 96px; }
  .card-back .wordmark .wordmark-line { font-size: 40px; }

  .contact {
    position: absolute; left: 80px; bottom: 74px;
    color: var(--black);
  }
  .contact-name {
    font-weight: 800; font-size: 34px; letter-spacing: 0.04em;
    text-transform: uppercase; line-height: 1.1;
  }
  .contact-role {
    font-weight: 700; font-size: 22px; color: var(--teal);
    letter-spacing: 0.05em; text-transform: uppercase;
    margin-bottom: 16px;
  }
  .contact-list { list-style: none; }
  .contact-item {
    display: flex; align-items: center; gap: 14px;
    font-size: 22px; font-weight: 500; line-height: 1.6;
  }
  .contact-icon { width: 20px; height: 20px; flex: none; }
</style>
</head>
<body>
<main class="stage">
  <section class="card card-front" aria-label="Card front">
    <h1 class="wordmark">
      <span class="wordmark-lead">BRIM</span>
      <span class="wordmark-line">Exterior</span>
      <span class="wordmark-line">Coatings</span>
    </h1>
  </section>

  <section class="card card-back" aria-label="Card back">
    <div class="contact">
      <p class="contact-name">Daniel Reyes</p>
      <p class="contact-role">CEO/Founder</p>
      <ul class="contact-list">
        <li class="contact-item">
          <svg class="contact-icon" viewBox="0 0 24 24" aria-hidden="true"><path fill="var(--teal)" d="M6.6 10.8c1.4 2.8 3.8 5.1 6.6 6.6l2.2-2.2c.3-.3.7-.4 1-.2 1.1.4 2.3.6 3.6.6.6 0 1 .4 1 1V20c0 .6-.4 1-1 1C10.6 21 3 13.4 3 4c0-.6.4-1 1-1h3.5c.6 0 1 .4 1 1 0 1.3.2 2.5.6 3.6.1.3 0 .7-.2 1z"/></svg>
          555-014-2980
        </li>
        <li class="contact-item">
          <svg class="contact-icon" viewBox="0 0 24 24" aria-hidden="true"><rect x="2" y="5" width="20" height="14" rx="1.5" fill="var(--teal)"/><path d="M3 6l9 7 9-7" fill="none" stroke="#fff" stroke-width="1.6"/></svg>
          daniel@brimcoatings.com
        </li>
        <li class="contact-item">
          <svg class="contact-icon" viewBox="0 0 24 24" aria-hidden="true"><g fill="none" stroke="var(--teal)" stroke-width="1.8"><circle cx="12" cy="12" r="9.5"/><ellipse cx="12" cy="12" rx="4" ry="9.5"/><path d="M2.5 12h19M4 7h16M4 17h16"/></g></svg>
          www.brimcoatings.com
        </li>
      </ul>
    </div>
    <h2 class="wordmark">
      <span class="wordmark-lead">BRIM</span>
      <span class="wordmark-line">Exterior</span>
      <span class="wordmark-line">Coatings</span>
    </h2>
  </section>
</main>
</body>
</html>
```